Business Card Design Project

Cyber Security. Company name is brightHarbor.

Industry/Entity Type

Computer Security

Contact Information for Business Card

Gregory Lindqvist
Founder and Chief Hacker

2370 W. Alder Rd.
Suite 514
Chicago, IL 60482
773.555.0196
gregory.lindqvist@brightharbor.example
www.brightharbor.example

```html
<!DOCTYPE html>
<html lang="en">
<head>
<meta charset="utf-8">
<title>brightHarbor Business Card</title>
<link href="https://fonts.googleapis.com/css2?family=Mulish:wght@300;400;500&display=swap" rel="stylesheet">
<style>
  :root {
    --navy: #1f2a44;
    --navy-soft: #3e4b63;
    --accent: #4a73e8;
    --ink: #1b1b1b;
    --paper: #ffffff;
  }
  html, body {
    margin: 0;
    padding: 0;
    width: 1200px;
    height: 1200px;
    overflow: hidden;
    background: var(--paper);
  }
  .card-sheet {
    display: block;
    width: 1200px;
    height: 1200px;
    font-family: "Mulish", sans-serif;
  }
  .front-face { fill: var(--navy); }
  .back-face { fill: var(--paper); }
  .faint-disc { fill: var(--navy-soft); }
  .wordmark { font-weight: 500; }
  .wordmark-light { fill: var(--paper); }
  .wordmark-dark { fill: var(--ink); }
  .mark-dot { fill: var(--accent); }
  .diagonal-blade { fill: var(--navy); }
  .person-name { fill: var(--accent); font-weight: 300; font-size: 40px; }
  .person-title { fill: var(--accent); font-weight: 400; font-size: 24px; }
  .icon-ring { fill: none; stroke: var(--accent); stroke-width: 2.5; }
  .icon-glyph { fill: var(--accent); }
  .icon-line { fill: none; stroke: var(--accent); stroke-width: 2; }
  .contact-text { fill: var(--ink); font-weight: 400; }
</style>
</head>
<body>
<svg class="card-sheet" viewBox="0 0 1200 1200" xmlns="http://www.w3.org/2000/svg">
  <defs>
    <filter id="blade-shadow" x="-50%" y="-10%" width="200%" height="120%">
      <feGaussianBlur in="SourceAlpha" stdDeviation="14"/>
      <feOffset dx="14" dy="6"/>
      <feComponentTransfer><feFuncA type="linear" slope="0.45"/></feComponentTransfer>
      <feFlood flood-color="#1f2a44"/>
      <feComposite operator="in" in2="SourceGraphic"/>
      <feMerge><feMergeNode/><feMergeNode in="SourceGraphic"/></feMerge>
    </filter>
  </defs>

  <!-- Front face -->
  <rect class="front-face" x="0" y="0" width="1200" height="660"/>
  <circle class="faint-disc" cx="278" cy="312" r="228" opacity="0.55"/>
  <circle class="mark-dot" cx="676" cy="314" r="34"/>
  <text class="wordmark wordmark-light" x="733" y="336" font-size="66">brightHarbor</text>

  <!-- Back face -->
  <rect class="back-face" x="0" y="660" width="1200" height="540"/>
  <circle class="mark-dot" cx="180" cy="930" r="28"/>
  <text class="wordmark wordmark-dark" x="224" y="948" font-size="48">brightHarbor</text>

  <polygon class="diagonal-blade" points="719,665 540,1182 645,1182" filter="url(#blade-shadow)"/>

  <text class="person-name" x="759" y="814" textLength="400" lengthAdjust="spacingAndGlyphs">GREGORY LINDQVIST</text>
  <text class="person-title" x="761" y="860" textLength="330" lengthAdjust="spacingAndGlyphs">FOUNDER AND CHIEF HACKER</text>

  <!-- Phone -->
  <circle class="icon-ring" cx="760" cy="945" r="21"/>
  <path class="icon-glyph" d="M752 934c2-1 4 0 5 2l2 4c1 1 0 3-1 4l-1 1c1 3 3 5 6 7l1-1c1-1 3-1 4 0l4 2c2 1 2 3 1 5l-2 2c-8 1-19-10-19-20z"/>
  <text class="contact-text" x="804" y="955" font-size="28">773.555.0196</text>

  <!-- Web -->
  <circle class="icon-ring" cx="760" cy="1017" r="21"/>
  <g class="icon-line">
    <circle cx="760" cy="1017" r="14"/>
    <ellipse cx="760" cy="1017" rx="6" ry="14"/>
    <line x1="746" y1="1017" x2="774" y2="1017"/>
    <line x1="748" y1="1010" x2="772" y2="1010"/>
    <line x1="748" y1="1024" x2="772" y2="1024"/>
  </g>
  <text class="contact-text" x="804" y="1025" font-size="25">www.brightharbor.example</text>

  <!-- Email -->
  <circle class="icon-ring" cx="760" cy="1089" r="21"/>
  <rect class="icon-glyph" x="749" y="1081" width="22" height="16" rx="2"/>
  <polyline points="749,1082 760,1091 771,1082" fill="none" stroke="#ffffff" stroke-width="2"/>
  <text class="contact-text" x="802" y="1096" font-size="18" textLength="360" lengthAdjust="spacingAndGlyphs">gregory.lindqvist@brightharbor.example</text>

  <!-- Address -->
  <circle class="icon-ring" cx="760" cy="1151" r="21"/>
  <path class="icon-line" d="M760 1167c-6-7-10-12-10-17a10 10 0 0 1 20 0c0 5-4 10-10 17z"/>
  <circle class="icon-line" cx="760" cy="1149" r="4"/>
  <text class="contact-text" x="804" y="1146" font-size="19">2370 W. Alder Rd., Suite 514</text>
  <text class="contact-text" x="804" y="1171" font-size="19">Chicago, IL 60482</text>
</svg>
</body>
</html>
```